label for a line of bbq rubs. my competition team name is copper kettle bbq *

i already have a logo, just need a label designed for a line of bbq rubs im developing. i want the design to be clean and eye catching and my colors of my logo are black and white. these will be sold in bbq specialty stores. i have a lot of traction in the bbq competition community, they are all familiar with my logo, just need a design that will stand out and draw attention to buys online and in the stores

Target Market(s)

backyard bbq cooks

Industry/Entity Type

Food blog

Font styles to use
Sans Serif

Colors

Designer to choose only greyscale colors for use in the design.

Requirements
Must have
• project must be simple, clean, with a classic look
Nice to have
• my logo, clean and simple

i have include some examples from other companies
Should not have
• cartoons

```html
<!DOCTYPE html>
<html lang="en">
<head>
<meta charset="utf-8">
<title>Copper Kettle BBQ – Rub Label</title>
<link href="https://fonts.googleapis.com/css2?family=Lato:wght@400;700;900&family=Roboto+Condensed:wght@400&family=Arimo:wght@400;700&display=swap" rel="stylesheet">
<style>
  :root {
    --backdrop: #97989c;
    --label-black: #000000;
    --paper: #ffffff;
    --silver-light: #e6e6e6;
    --silver-mid: #9a9a9a;
    --silver-dark: #3a3a3a;
    --meat-deep: #4a1a0c;
    --meat-glaze: #b8411a;
    --meat-amber: #d9782a;
    --ink: #000000;
  }
  * { box-sizing: border-box; margin: 0; padding: 0; }
  html, body {
    width: 1200px; height: 441px; overflow: hidden;
    background: var(--backdrop);
  }
  .label {
    position: absolute; left: 67px; top: 50px;
    width: 1066px; height: 340px;
    background: var(--label-black);
    color: var(--paper);
    font-family: "Lato", sans-serif;
  }
  .trim-line {
    position: absolute; left: 0; width: 100%; height: 3px;
    background: linear-gradient(90deg, var(--silver-dark) 0%, var(--silver-light) 20%, var(--silver-mid) 45%, var(--silver-light) 70%, var(--silver-dark) 100%);
  }
  .trim-line--top { top: 13px; }
  .trim-line--bottom { top: 325px; }

  /* left story panel */
  .story { position: absolute; left: 26px; top: 0; width: 304px; }
  .story__title {
    position: absolute; top: 32px; left: 0;
    font-size: 14.5px; font-weight: 400; letter-spacing: 0.2px; white-space: nowrap;
  }
  .story__text {
    position: absolute; left: 0; width: 304px;
    font-size: 10.2px; line-height: 12.4px; text-align: justify;
  }
  .story__text--intro { top: 57px; }
  .story__text--closing { top: 195px; }
  .story__callout {
    position: absolute; left: -1px; top: 129px; width: 306px; height: 54px;
    border: 1.5px solid var(--paper);
    padding: 6px 7px 0 7px;
    font-size: 10.2px; line-height: 12.4px; text-align: justify;
  }
  .code-box {
    position: absolute; left: 26px; top: 248px; width: 136px; height: 69px;
    background: var(--paper); color: var(--ink);
    display: flex; align-items: center; justify-content: center;
    font-size: 12.5px; font-weight: 700;
  }
  .date-field { position: absolute; left: 172px; font-size: 10.5px; white-space: nowrap; }
  .date-field--issue { top: 251px; }
  .date-field--exp { top: 284px; }

  /* centre brand */
  .banner { position: absolute; left: 418px; top: 0; width: 228px; height: 180px; }
  .brand {
    position: absolute; left: 421px; width: 222px; text-align: center;
    font-family: "Lato", sans-serif; font-weight: 900; color: var(--ink);
    line-height: 1; white-space: nowrap;
  }
  .brand--name { top: 42px; font-size: 19.5px; letter-spacing: 0.3px; }
  .brand--bbq { top: 62px; font-size: 86px; letter-spacing: -3px; }
  .variety {
    position: absolute; left: 421px; width: 222px; top: 172px;
    text-align: center; font-size: 19px; line-height: 23px; font-weight: 400;
  }
  .product-shot {
    position: absolute; left: 464px; top: 225px; width: 170px; height: 98px;
    border-radius: 40% 55% 45% 50% / 50% 45% 55% 50%;
    background: radial-gradient(ellipse at 60% 50%, var(--meat-glaze) 0%, var(--meat-amber) 35%, var(--meat-deep) 75%, transparent 100%);
  }
  .net-weight {
    position: absolute; left: 421px; top: 269px; width: 48px; height: 71px;
    background: var(--paper); color: var(--ink);
    border-top-right-radius: 26px;
    padding: 14px 0 0 6px;
    font-size: 9.5px; line-height: 11.5px; font-weight: 700;
  }

  /* claims column */
  .claims { position: absolute; left: 733px; top: 0; width: 60px; }
  .claim { position: absolute; left: 0; width: 60px; text-align: center; }
  .claim__seal {
    display: block; margin: 0 auto;
    width: 35px; height: 35px; border-radius: 50%;
    border: 2px solid var(--paper);
  }
  .claim__name {
    display: block; margin-top: 4px; margin-left: -15px; width: 90px;
    font-family: "Roboto Condensed", sans-serif; font-size: 10.5px; white-space: nowrap;
  }
  .claim--gluten { top: 42px; }
  .claim--gmo { top: 110px; }
  .claim--halal { top: 177px; }
  .claim--kosher { top: 247px; }

  /* nutrition panel */
  .nutrition {
    position: absolute; left: 811px; top: 29px; width: 217px; height: 283px;
    background: var(--paper); padding: 4px 6px; color: var(--ink);
    font-family: "Arimo", sans-serif;
  }
  .nutrition__frame { border: 1px solid var(--ink); height: 100%; padding: 0 3px; }
  .nutrition__title { font-size: 21px; font-weight: 700; letter-spacing: 2.6px; line-height: 24px; white-space: nowrap; }
  .nutrition__serving { font-size: 8.4px; line-height: 10px; }
  .rule-heavy { height: 3px; background: var(--ink); margin: 1px 0; }
  .rule-mid { height: 2px; background: var(--ink); margin: 1px 0; }
  .nutrition__row {
    display: flex; justify-content: space-between;
    font-size: 8.5px; line-height: 12.3px; height: 12.4px;
    border-bottom: 0.6px solid #777;
  }
  .nutrition__row--small { font-size: 6.8px; font-weight: 700; line-height: 9px; height: 9.4px; }
  .nutrition__row--dv { justify-content: flex-end; font-size: 6.5px; font-weight: 700; line-height: 10px; height: 10px; }
  .nutrition__row--sub { padding-left: 12px; }
  .nutrition__row--last { border-bottom: none; }
  .nutrition__row b { font-weight: 700; }
  .nutrition__row .pct { font-weight: 700; }
  .nutrition__note { font-size: 6.2px; line-height: 7.6px; text-align: center; margin-top: 2px; }
  .nutrition__table {
    width: 100%; border-collapse: collapse; margin-top: 2px;
    font-size: 6px; line-height: 8.7px; border-top: 0.6px solid var(--ink);
  }
  .nutrition__table td { padding: 0; white-space: nowrap; }
  .nutrition__table .indent { padding-left: 4px; }
</style>
</head>
<body>
<main class="label">
  <div class="trim-line trim-line--top"></div>
  <div class="trim-line trim-line--bottom"></div>

  <section class="story">
    <h2 class="story__title">LOREM IPSUM</h2>
    <p class="story__text story__text--intro">Lorem ipsum dolor sit amet, consectetuer adipiscing elit, sed diam nonummy nibh euismod tincidunt ut laoreet dolore magna aliquam erat volutpat. Ut wisi enim ad minim veniam, quis nostrud exerci tation ullamcorper suscipit lobortis nisl ut aliquip ex ea commodo consequat. Duis autem vel eum iriure dolor.</p>
    <p class="story__callout">Lorem ipsum dolor sit amet, consectetuer adipiscing elit, sed diam nonummy nibh euismod tincidunt ut laoreet dolore magna aliquam erat volutpat. Ut wisi enim ad minim veniam.</p>
    <p class="story__text story__text--closing">Lorem ipsum dolor sit amet, consectetuer adipiscing elit, sed diam nonummy nibh euismod tincidunt ut laoreet dolore magna aliquam erat volutpat. Ut wisi enim ad minim veniam</p>
  </section>

  <div class="code-box">bar code</div>
  <p class="date-field date-field--issue">Issue Date:</p>
  <p class="date-field date-field--exp">Exp Date:</p>

  <svg class="banner" viewBox="0 0 228 180" aria-hidden="true">
    <defs>
      <linearGradient id="bannerEdge" x1="0" x2="1" y1="0" y2="0">
        <stop offset="0" stop-color="#e6e6e6"/>
        <stop offset="0.5" stop-color="#8a8a8a"/>
        <stop offset="1" stop-color="#e6e6e6"/>
      </linearGradient>
    </defs>
    <polygon points="0,0 228,0 228,177 114,153 0,177" fill="url(#bannerEdge)"/>
    <polygon points="3,0 225,0 225,172 114,150 3,172" fill="#ffffff"/>
  </svg>
  <p class="brand brand--name">COPPER KETTLE</p>
  <p class="brand brand--bbq">BBQ</p>

  <p class="variety">BRISKET<br>RIBS &amp; CHICKEN</p>
  <div class="product-shot" role="img" aria-label="Glazed barbecue chicken leg quarter"></div>
  <p class="net-weight">Net wt<br>11 Oz<br>(312g)</p>

  <aside class="claims">
    <div class="claim claim--gluten"><span class="claim__seal"></span><span class="claim__name">Gluten Free</span></div>
    <div class="claim claim--gmo"><span class="claim__seal"></span><span class="claim__name">Non GMO</span></div>
    <div class="claim claim--halal"><span class="claim__seal"></span><span class="claim__name">Halal Certified</span></div>
    <div class="claim claim--kosher"><span class="claim__seal"></span><span class="claim__name">Kosher Certified</span></div>
  </aside>

  <section class="nutrition">
    <div class="nutrition__frame">
      <h3 class="nutrition__title">Nutrition Facts</h3>
      <p class="nutrition__serving">Serving Size 1 (44g)</p>
      <div class="rule-heavy"></div>
      <div class="nutrition__row nutrition__row--small"><span>Amount Per Serving</span></div>
      <div class="nutrition__row"><span><b>Calories</b> 96</span></div>
      <div class="rule-mid"></div>
      <div class="nutrition__row nutrition__row--dv"><span>% Daily Values*</span></div>
      <div class="nutrition__row"><span><b>Total Fat</b> 1g</span><span class="pct">2%</span></div>
      <div class="nutrition__row nutrition__row--sub"><span>Saturated Fat 0g</span><span class="pct">0%</span></div>
      <div class="nutrition__row nutrition__row--sub"><span>Trans Fat 0g</span><span></span></div>
      <div class="nutrition__row"><span><b>Cholesterol</b> 0mg</span><span class="pct">0%</span></div>
      <div class="nutrition__row"><span><b>Sodium</b> 1mg</span><span class="pct">0%</span></div>
      <div class="nutrition__row"><span><b>Total Carbohydrate</b> 22g</span><span class="pct">7%</span></div>
      <div class="nutrition__row nutrition__row--sub"><span>Dietary Fiber 0g</span><span class="pct">0%</span></div>
      <div class="nutrition__row nutrition__row--sub"><span>Sugars 6g</span><span></span></div>
      <div class="nutrition__row nutrition__row--last"><span><b>Protein</b> 1g</span><span class="pct">2%</span></div>
      <div class="rule-heavy"></div>
      <p class="nutrition__note">*Percent Daily Values are based on a 2,000 calorie diet. Your Daily Values may be higher or lower depending on your calorie needs.</p>
      <table class="nutrition__table">
        <tr><td></td><td>Calories</td><td>2,000</td><td>2,500</td></tr>
        <tr><td>Total Fat</td><td>Less than</td><td>65g</td><td>80g</td></tr>
        <tr><td class="indent">Sat Fat</td><td>Less than</td><td>20g</td><td>25g</td></tr>
        <tr><td>Cholesterol</td><td>Less than</td><td>300mg</td><td>300mg</td></tr>
        <tr><td>Sodium</td><td>Less than</td><td>2400mg</td><td>2400mg</td></tr>
        <tr><td>Total Carbohydrate</td><td></td><td>300g</td><td>375g</td></tr>
        <tr><td class="indent">Dietary Fiber</td><td></td><td>25g</td><td>30g</td></tr>
      </table>
    </div>
  </section>
</main>
</body>
</html>
```